Vantri Almond Protein - Less, but better

Design a protein powder pouch (350g). Take inspiration from Parvenix.co and put the same information on the pouch and add "made in Australia". I do not want it to be exactly the same design but just take some inspiration from it.

```html
<!DOCTYPE html>
<html lang="en">
<head>
<meta charset="utf-8">
<title>Vantri Almond Protein Powder – Real Vanilla</title>
<link rel="stylesheet" href="https://fonts.googleapis.com/css2?family=Quicksand:wght@700&family=Montserrat:wght@700;800&family=Nunito:wght@400;800&family=Questrial&display=swap">
<style>
  :root {
    --forest: #213a33;
    --cream: #f6f3e8;
    --blush: #e3a39e;
    --saffron: #f0a422;
    --ink: #000000;
    --mist: #e6e7e8;
    --paper: #ffffff;
  }
  * { margin: 0; padding: 0; box-sizing: border-box; }
  html, body { width: 756px; height: 1200px; overflow: hidden; background: var(--paper); }
  .pouch { position: relative; width: 756px; height: 1200px; overflow: hidden; background: var(--paper); }

  .brand-band {
    position: absolute; left: 0; top: 0; width: 756px; height: 445px;
    background: var(--forest); color: var(--cream); text-align: center;
  }
  .brand-name {
    position: absolute; top: 222px; width: 100%;
    font-family: "Quicksand", sans-serif; font-weight: 700;
    font-size: 104px; line-height: 1; letter-spacing: -1px;
  }
  .tagline {
    position: absolute; top: 357px; width: 100%;
    font-family: "Questrial", sans-serif; font-size: 27px; letter-spacing: 4px; color: var(--paper);
  }
  .origin {
    position: absolute; top: 397px; width: 100%;
    font-family: "Montserrat", sans-serif; font-weight: 700; font-size: 20px;
    font-variant: small-caps; text-transform: lowercase; letter-spacing: 1px; color: var(--paper);
  }
  .origin .cap { text-transform: none; }

  .pattern-field {
    position: absolute; left: 0; top: 445px; width: 756px; height: 755px;
    background:
      radial-gradient(circle at 20% 25%, rgba(227,163,158,.55), transparent 30%),
      radial-gradient(circle at 85% 55%, rgba(240,164,34,.45), transparent 30%),
      radial-gradient(circle at 15% 80%, rgba(240,164,34,.4), transparent 28%),
      linear-gradient(180deg, #2a3b35 0%, #5c5f58 50%, #3a3c37 100%);
  }

  .product-label {
    position: absolute; left: 170px; top: 467px; width: 416px; height: 436px;
    background: var(--paper); border: 4px dotted var(--forest); border-radius: 6px;
  }
  .product-title {
    position: absolute; left: 183px; top: 483px; width: 389px; height: 252px;
    background: var(--forest); border-radius: 14px 14px 28px 0;
    color: var(--paper); text-align: center;
    font-family: "Montserrat", sans-serif; font-weight: 800; font-size: 67px; line-height: 72px;
    padding-top: 17px; letter-spacing: -1px;
  }
  .dot-rule {
    position: absolute; left: 196px; width: 364px; border-top: 6px dotted var(--forest);
  }
  .dot-rule--upper { top: 756px; }
  .dot-rule--lower { top: 820px; left: 184px; }
  .flavour {
    position: absolute; left: 183px; top: 771px; width: 389px; height: 38px;
    background: var(--forest); border-radius: 10px 10px 14px 0;
    color: var(--saffron); text-align: center;
    font-family: "Montserrat", sans-serif; font-weight: 800; font-size: 30px; line-height: 38px;
  }
  .claim {
    position: absolute; left: 170px; top: 840px; width: 416px; text-align: center; color: var(--forest);
  }
  .claim-main { font-family: "Montserrat", sans-serif; font-weight: 800; font-size: 21px; line-height: 26px; }
  .claim-sub { font-family: "Questrial", sans-serif; font-size: 18px; font-variant: small-caps; line-height: 22px; }

  .net-weight {
    position: absolute; left: 300px; top: 920px; width: 160px; height: 160px;
    border-radius: 50%; background: var(--blush); color: var(--ink); text-align: center;
    font-family: "Nunito", sans-serif; font-weight: 800; font-size: 22px; line-height: 24px;
    padding-top: 88px;
  }
  .benefits {
    position: absolute; left: 88px; top: 930px; width: 579px; height: 71px;
    background: var(--blush); border-radius: 12px; text-align: center; color: var(--forest);
    font-family: "Nunito", sans-serif; padding-top: 8px;
  }
  .benefits-title { font-weight: 800; font-size: 20px; line-height: 26px; }
  .benefits-list { font-weight: 400; font-size: 20px; line-height: 26px; }
</style>
</head>
<body>
<main class="pouch">
  <header class="brand-band">
    <h1 class="brand-name">vantri</h1>
    <p class="tagline">– less, but better –</p>
    <p class="origin">made in <span class="cap">A</span>ustralia</p>
  </header>

  <div class="pattern-field" role="img" aria-label="Geometric pattern of half circles in forest green, blush pink, saffron, black and grey"></div>

  <section class="product-label"></section>
  <h2 class="product-title">ALMOND<br>PROTEIN<br>POWDER</h2>
  <div class="dot-rule dot-rule--upper"></div>
  <p class="flavour">REAL VANILLA</p>
  <div class="dot-rule dot-rule--lower"></div>
  <div class="claim">
    <p class="claim-main">VEGAN &amp; DELICIOUS</p>
    <p class="claim-sub">Just 4 Ingredients</p>
  </div>

  <div class="net-weight">Net Weight<br>350g</div>
  <div class="benefits">
    <p class="benefits-title">Naturally Supports Health:</p>
    <p class="benefits-list">Heart • Digestion • Immune System • Skin • Bone • Hair</p>
  </div>
</main>
</body>
</html>
```